Stonebell Inc Ad Design, trying to attract new customers

Please see attached pictures and files for information
We are a Class A - Residential General Contractor in Lynchburg, VA with Master HVAC and Master PLUMBING Licenses. We focus on Water and Air Solutions for property owners.
We build, remodel, and repair homes
We do HVAC, including Humidity Control and Air Purification
We do Plumbing
We love to fix Water Leaks for Plumbing, Roof Leaks, Skylight Leaks, Basement Leaks, Foundation Leaks, Door and Window Leaks
We solve water and air issues on the outside of properties with custom structures, grading, and landscaping

Target Market(s)

Residential and Light Commercial property owners

Industry/Entity Type

Construction

Font styles to use
Other font styles liked:
• see cards

Colors
0054AA
0677BA
7BADD7
CADEEF
E8F1F8
00AB8E
00BBA5
67D7C9
C6EFE9
E9F9F6

Requirements
Must have
• See business cards
Nice to have
• see business cards
Should not have
• My name

```html
<!DOCTYPE html>
<html lang="en">
<head>
<meta charset="utf-8">
<title>Stonebell Inc – Water and Air Solutions</title>
<link href="https://fonts.googleapis.com/css2?family=Roboto:wght@400;500;700&display=swap" rel="stylesheet">
<style>
  :root {
    --stage: #787e81;
    --paper: #ffffff;
    --green-dark: #23913f;
    --green-light: #8cc63f;
    --blue-dark: #175c99;
    --blue-mid: #1b7fc0;
    --blue-light: #22a6e0;
    --ink: #4a4a4a;
    --white: #ffffff;
  }
  * { box-sizing: border-box; margin: 0; padding: 0; }
  html, body { width: 1200px; height: 1200px; overflow: hidden; }
  body { background: var(--stage); font-family: "Roboto", sans-serif; position: relative; }

  .ad {
    position: absolute; left: 87px; top: 343px;
    width: 1026px; height: 514px;
    background: var(--paper);
    overflow: hidden;
    box-shadow: 2px 2px 3px rgba(0,0,0,.45);
  }
  .ad-shapes { position: absolute; inset: 0; width: 100%; height: 100%; }

  .intro { position: absolute; left: 57px; top: 46px; width: 240px; color: var(--white); }
  .intro-lead { font-size: 14px; line-height: 18px; font-weight: 400; }
  .intro-focus { margin-top: 8px; font-size: 22.5px; line-height: 24.5px; font-weight: 700; }

  .services-title {
    position: absolute; left: 51px; top: 243px; width: 206px; height: 34px;
    border-radius: 17px;
    background: linear-gradient(90deg, var(--blue-dark), var(--blue-light));
    color: var(--white); font-weight: 700; font-size: 30px; line-height: 34px;
    padding-left: 6px;
  }
  .services-list { position: absolute; left: 53px; top: 292px; width: 520px; list-style: none; }
  .services-list li {
    position: relative; padding-left: 32px;
    color: var(--ink); font-size: 16.2px; line-height: 22.4px;
    margin-bottom: 4.3px;
  }
  .services-list li svg { position: absolute; left: 0; top: 3px; width: 17px; height: 17px; }

  .brand {
    position: absolute; left: 640px; top: 66px; width: 280px;
    display: flex; align-items: center; justify-content: center; gap: 10px;
  }
  .brand-dot { width: 26px; height: 26px; border-radius: 50%; background: var(--blue-mid); }
  .brand-name { font-size: 30px; font-weight: 700; color: var(--blue-mid); letter-spacing: 1px; }

  .tagline {
    position: absolute; left: 520px; top: 148px; width: 520px; text-align: center;
    font-weight: 700; font-size: 27px; line-height: 34px;
  }
  .tagline-quote { color: var(--blue-dark); }
  .tagline-class { color: var(--green-dark); }

  .specialties {
    position: absolute; left: 666px; top: 260px; width: 270px; text-align: center;
    color: var(--white); font-size: 15px; line-height: 19px;
  }

  .contact-phone {
    position: absolute; left: 604px; top: 418px;
    display: flex; align-items: center; gap: 14px;
    color: var(--white); font-weight: 700; font-size: 41px; line-height: 50px;
  }
  .contact-phone svg { width: 35px; height: 35px; }
  .contact-email {
    position: absolute; left: 659px; top: 477px;
    display: flex; align-items: center; gap: 9px;
    color: var(--white); font-size: 17.5px; line-height: 22px;
  }
  .contact-email svg { width: 18px; height: 13px; }
</style>
</head>
<body>
<main class="ad">
  <svg class="ad-shapes" viewBox="0 0 1652 828" preserveAspectRatio="none" aria-hidden="true">
    <defs>
      <linearGradient id="leafGreen" x1="0" x2="1" y1="0" y2="0">
        <stop offset="0" stop-color="#23913f"/>
        <stop offset="1" stop-color="#8cc63f"/>
      </linearGradient>
      <linearGradient id="seaBlue" x1="0" x2="1" y1="0" y2="0">
        <stop offset="0" stop-color="#175c99"/>
        <stop offset="1" stop-color="#22a6e0"/>
      </linearGradient>
      <linearGradient id="bandBlue" x1="0" x2="1">
        <stop offset="0" stop-color="#1b7fc0"/>
        <stop offset="1" stop-color="#22a6e0"/>
      </linearGradient>
    </defs>
    <!-- top-left green leaf -->
    <path d="M0,110 C100,35 240,15 330,25 C450,45 540,130 605,238 C480,330 330,385 200,368 C110,355 45,330 0,305 Z" fill="url(#leafGreen)"/>
    <!-- green swoosh tail -->
    <path d="M605,238 C720,330 840,450 945,540 C850,470 720,360 605,238 Z" fill="#5bb146"/>
    <!-- bottom-right blue field -->
    <path d="M895,828 C895,720 920,620 975,545 C1080,630 1200,655 1300,655 C1450,655 1570,600 1652,470 L1652,828 Z" fill="url(#seaBlue)"/>
    <!-- blue sweeping band -->
    <path d="M35,72 C160,-20 330,-5 440,55 C620,150 780,380 960,520 C1080,615 1200,640 1310,640 C1460,640 1580,560 1652,458" fill="none" stroke="url(#bandBlue)" stroke-width="14"/>
    <!-- right green lens -->
    <path d="M980,528 C1060,420 1180,370 1295,370 C1420,370 1530,430 1600,518 C1520,600 1420,643 1300,643 C1180,643 1060,590 980,528 Z" fill="url(#leafGreen)" stroke="#ffffff" stroke-width="4"/>
  </svg>

  <section class="intro">
    <p class="intro-lead">We are a Class A - Residential General Contractor in Lynchburg, VA with Master HVAC and Master PLUMBING Licenses.</p>
    <p class="intro-focus">We focus on Water and Air Solutions for property owners.</p>
  </section>

  <h2 class="services-title">Our Services</h2>
  <ul class="services-list">
    <li><svg viewBox="0 0 20 20"><circle cx="10" cy="10" r="10" fill="#175c99"/><path d="M5.5 10.3l3 3 6-6.3" fill="none" stroke="#fff" stroke-width="2.4" stroke-linecap="round" stroke-linejoin="round"/></svg>We build, remodel, and repair homes</li>
    <li><svg viewBox="0 0 20 20"><circle cx="10" cy="10" r="10" fill="#175c99"/><path d="M5.5 10.3l3 3 6-6.3" fill="none" stroke="#fff" stroke-width="2.4" stroke-linecap="round" stroke-linejoin="round"/></svg>We do HVAC, including Humidity Control and Air Purification</li>
    <li><svg viewBox="0 0 20 20"><circle cx="10" cy="10" r="10" fill="#175c99"/><path d="M5.5 10.3l3 3 6-6.3" fill="none" stroke="#fff" stroke-width="2.4" stroke-linecap="round" stroke-linejoin="round"/></svg>We do Plumbing</li>
    <li><svg viewBox="0 0 20 20"><circle cx="10" cy="10" r="10" fill="#175c99"/><path d="M5.5 10.3l3 3 6-6.3" fill="none" stroke="#fff" stroke-width="2.4" stroke-linecap="round" stroke-linejoin="round"/></svg>We love to fix Water Leaks for Plumbing, Roof Leaks, Skylight Leaks, Basement Leaks, Foundation Leaks, Door and Window Leaks</li>
    <li><svg viewBox="0 0 20 20"><circle cx="10" cy="10" r="10" fill="#175c99"/><path d="M5.5 10.3l3 3 6-6.3" fill="none" stroke="#fff" stroke-width="2.4" stroke-linecap="round" stroke-linejoin="round"/></svg>We solve water and air issues on the outside of properties with custom structures, grading, and landscaping</li>
  </ul>

  <div class="brand">
    <span class="brand-dot"></span>
    <span class="brand-name">STONEBELL</span>
  </div>

  <p class="tagline">
    <span class="tagline-quote">"We put Water and Air in its Place"</span><br>
    <span class="tagline-class">Class A RBC PLUMBINGHVAC</span>
  </p>

  <p class="specialties">Humidity Control/<br>Air Purification, Roof/Skylight Leaks, Basement/Foundation Leaks, Drain-age/Grading/Landscaping, Custom Outdoor Structures - Porches, Decks, Sunrooms, Gazebos</p>

  <p class="contact-phone">
    <svg viewBox="0 0 36 36"><circle cx="18" cy="18" r="17" fill="#5bb146" stroke="#fff" stroke-width="2"/><path d="M12.5 9.5c1-.6 2-.3 2.5.6l1.5 2.8c.4.8.2 1.6-.5 2.1l-1.2.9c.9 2.2 2.5 3.9 4.6 4.9l1-1.2c.5-.6 1.4-.8 2.1-.4l2.8 1.6c.9.5 1.1 1.6.5 2.5-1.1 1.7-2.8 2.5-4.7 1.9-5-1.6-8.8-5.5-10.3-10.5-.5-1.9.2-3.9 1.7-5.2z" fill="#fff"/></svg>
    (434) 555-0182
  </p>
  <p class="contact-email">
    <svg viewBox="0 0 18 13"><rect width="18" height="13" rx="1.5" fill="#fff"/><path d="M1 1.5l8 6 8-6" fill="none" stroke="#1b7fc0" stroke-width="1.6"/></svg>
    Contact@StonebellVA.com
  </p>
</main>
</body>
</html>
```